Anzeigengestaltung für einen Burgerladen in Karlsruhe
Zielgruppe
Bei dem Projekt handelt es sich um einen super Burgerladen in Karlsruhe.
Aufgabenstellung
Datei-Typ: pdf oder jpeg
Format: A5
Farbe: ja
Schnittzugabe: 3mm
Bild wie im Anhang. Die Info.
Text:
Focus: Bei uns gibts Scheine auch ohne Vorlesung.
Studentenjob* gesucht? Bei uns gibts Scheine auch ohne Vorlesung.
Individuelle Arbeitszeiten – Free Food - Faire Bezahlung – Ziemlich tolle Kollegen.
Foto: Dort würde ich eine Art kleinen Kasten einsetzen lassen:
Timo, 24 Griller und guter Typ
Bewirb dich einfach, unkompliziert als Griller / Multitalent. Keine Erfahrung? Kein Problem. Timo und Deine neuen Kollegen zeigen dir alles.
*(m/w/d)

```html
<!DOCTYPE html>
<html lang="de">
<head>
<meta charset="utf-8">
<title>Glutwerk Burgers – Griller / Multitalent gesucht</title>
<link rel="stylesheet" href="https://fonts.googleapis.com/css2?family=Jost:ital,wght@0,300;0,400;0,500;0,700;0,800;1,500&display=swap">
<style>
  :root {
    --kraft: #a67c55;
    --paper: #ffffff;
    --ink: #1a1a1a;
    --photo-top: #b9c3cc;
    --photo-bottom: #5a3a3e;
    --tool-tone: #d9d9d9;
  }
  * { margin: 0; padding: 0; box-sizing: border-box; }
  html, body { width: 846px; height: 1200px; overflow: hidden; }
  body { font-family: "Jost", "Futura", sans-serif; color: var(--ink); background: var(--kraft); }

  .poster { position: relative; width: 846px; height: 1200px; overflow: hidden; background: var(--kraft); }
  .paper-band { position: absolute; inset: 0; width: 846px; height: 1200px; }

  .brand {
    position: absolute; top: 82px; left: 0; width: 846px; text-align: center;
    font-weight: 700; font-size: 76px; line-height: 90px; color: var(--paper);
  }

  .kicker {
    position: absolute; top: 286px; left: 0; width: 846px; text-align: center;
    font-weight: 300; font-size: 30px; line-height: 36px; letter-spacing: 0.5px;
  }
  .job-title {
    position: absolute; left: 208px; top: 336px;
    font-weight: 700; font-size: 65px; line-height: 64px; letter-spacing: 1px;
  }
  .job-title .line-one { display: block; padding-left: 70px; }
  .job-title .line-two { display: block; }
  .gender { font-weight: 300; font-size: 25px; letter-spacing: 0; margin-left: 10px; }

  .divider { position: absolute; top: 494px; left: 0; width: 846px; }

  .benefits {
    position: absolute; left: 60px; top: 550px; width: 430px;
    font-weight: 700; font-size: 21px; line-height: 29px; letter-spacing: 0.4px; text-transform: uppercase;
  }
  .pitch {
    position: absolute; left: 60px; top: 655px; width: 420px;
    font-weight: 400; font-size: 21px; line-height: 32px;
  }

  .pointer { position: absolute; left: 328px; top: 792px; }

  .caption {
    position: absolute; left: 300px; width: 180px; top: 852px; text-align: center;
    font-style: italic; font-weight: 500; font-size: 17px; line-height: 23px;
  }

  .grill-tools {
    position: absolute; left: 44px; top: 852px; width: 232px; height: 146px;
    background: var(--tool-tone); border-radius: 6px;
  }

  .team-photo {
    position: absolute; left: 494px; top: 528px; width: 372px; height: 478px;
    background: var(--paper); padding: 10px;
    transform: rotate(1.6deg); box-shadow: 0 2px 6px rgba(0,0,0,0.25);
  }
  .team-photo .photo-fill {
    width: 100%; height: 100%;
    background: linear-gradient(165deg, var(--photo-top) 0%, #8d8f96 45%, var(--photo-bottom) 100%);
  }

  .contact {
    position: absolute; top: 1010px; left: 0; width: 846px; text-align: center; color: var(--paper);
    font-size: 21px; line-height: 31px;
  }
  .contact .contact-head { font-weight: 700; font-size: 22px; letter-spacing: 0.8px; }
  .contact strong { font-weight: 700; }
</style>
</head>
<body>
<main class="poster">
  <svg class="paper-band" viewBox="0 0 846 1200" aria-hidden="true">
    <polygon points="0,266 846,218 846,958 0,1012" fill="var(--paper)"/>
  </svg>

  <div class="brand">Glutwerk Burgers</div>

  <p class="kicker">STUDENTENJOB GESUCHT?</p>
  <h1 class="job-title">
    <span class="line-one">GRILLER /</span>
    <span class="line-two">MULTITALENT<span class="gender">(m/w/d)</span></span>
  </h1>

  <svg class="divider" width="846" height="14" viewBox="0 0 846 14" aria-hidden="true">
    <circle cx="409" cy="7" r="5" fill="var(--ink)"/>
    <circle cx="423" cy="7" r="5" fill="var(--ink)"/>
    <circle cx="437" cy="7" r="5" fill="var(--ink)"/>
  </svg>

  <h2 class="benefits">Individuelle Arbeitszeiten –<br>Free Food – Faire Bezahlung –<br>Ziemlich tolle Kollegen</h2>

  <p class="pitch">Hier gibt es Scheine auch ohne Vorlesung.<br>Bewirb dich einfach, unkompliziert als<br>Griller / Multitalent. Keine Erfahrung?<br>Kein Problem. Timo und deine neuen<br>Kollegen zeigen dir alles.</p>

  <svg class="pointer" width="160" height="60" viewBox="0 0 160 60" aria-hidden="true">
    <path d="M5 5 C 25 45, 95 52, 148 38" fill="none" stroke="var(--ink)" stroke-width="4" stroke-linecap="round"/>
    <path d="M132 26 L150 37 L134 50" fill="none" stroke="var(--ink)" stroke-width="4" stroke-linecap="round" stroke-linejoin="round"/>
  </svg>

  <p class="caption">TIMO, 24<br>Griller und guter Typ</p>

  <div class="grill-tools" role="img" aria-label="Gekreuzte Grillgabel und Grillwender als Illustration"></div>

  <figure class="team-photo">
    <div class="photo-fill" role="img" aria-label="Foto: Timo, lächelnder Griller mit Cap und Schürze in der Küche"></div>
  </figure>

  <section class="contact">
    <p class="contact-head">DEIN KONTAKT ZU UNS:</p>
    <p>Marlene - Stellvertretung des Inhabers</p>
    <p><strong>0721 48 27 51 93</strong> oder <strong>info@glutwerk-burgers.de</strong></p>
  </section>
</main>
</body>
</html>
```